Advertisement Design

I'm looking for a post card sized advertisement piece that I will be dropping off to commercial and residential customers.
On one side I want it promoting carpet cleaning services and on the other side dryer vent cleaning services.
I've uploaded two different layouts of my company logo for you to choice from.
One batch will be printed with my Michigan Number
One batch will be printed with my Tennessee number
Will share contact numbers with the winner so just use a make up number
555-319-4826

Slow in providing feedback

```html
<!DOCTYPE html>
<html lang="en">
<head>
<meta charset="utf-8">
<title>Tidewell Property Services – Carpet Cleaning</title>
<link href="https://fonts.googleapis.com/css2?family=Exo+2:ital,wght@0,500;0,600;1,400;1,500;1,800&family=Montserrat:wght@500;600&display=swap" rel="stylesheet">
<style>
  :root {
    --brand-blue: #3b7fb6;
    --deep-blue: #2f6fa8;
    --teal: #3fb3d3;
    --text-blue: #2b6aa3;
    --white: #ffffff;
  }
  * { box-sizing: border-box; margin: 0; padding: 0; }
  html, body { width: 927px; height: 1200px; overflow: hidden; background: var(--white); }
  .flyer {
    position: relative;
    width: 927px;
    height: 1200px;
    overflow: hidden;
    background: var(--white);
    font-family: "Exo 2", sans-serif;
  }
  .hero { position: absolute; left: 0; top: 0; width: 927px; height: 830px; }
  .hero svg { display: block; }
  .brand-panel {
    position: absolute;
    left: 0; top: 0;
    width: 509px; height: 294px;
    background: var(--white);
    border-radius: 0 46px 46px 0;
  }
  .brand-mark {
    position: absolute;
    left: 204px; top: 68px;
    width: 102px; height: 102px;
    background: var(--brand-blue);
    border-radius: 10px;
  }
  .brand-name {
    position: absolute;
    left: 0; top: 186px;
    width: 509px;
    text-align: center;
    font-family: "Exo 2", sans-serif;
    font-weight: 500;
    color: var(--deep-blue);
  }
  .brand-name .brand-main {
    display: block;
    font-size: 48px;
    line-height: 52px;
    letter-spacing: 0.04em;
  }
  .brand-name .brand-sub {
    display: block;
    margin-top: 2px;
    font-size: 14px;
    line-height: 18px;
    letter-spacing: 0.22em;
  }
  .hero-copy {
    position: absolute;
    left: 0; top: 474px;
    width: 927px;
    text-align: center;
    color: var(--white);
  }
  .headline {
    font-style: italic;
    font-weight: 800;
    font-size: 52px;
    line-height: 69px;
    letter-spacing: -0.01em;
  }
  .subline {
    margin: 24px auto 0;
    width: 640px;
    font-style: italic;
    font-weight: 500;
    font-size: 20px;
    line-height: 31px;
  }
  .audiences {
    position: absolute;
    left: 0; top: 830px;
    width: 927px;
  }
  .audience { position: absolute; top: 0; width: 440px; text-align: center; }
  .audience-residential { left: 27px; }
  .audience-commercial { left: 490px; }
  .audience-title {
    font-family: "Montserrat", sans-serif;
    font-weight: 600;
    font-size: 25px;
    line-height: 24px;
    letter-spacing: 0.3em;
    color: var(--teal);
    text-transform: uppercase;
    margin-bottom: 26px;
  }
  .benefits { list-style: none; margin: 0 auto; width: 410px; }
  .benefits li {
    font-style: italic;
    font-size: 13.5px;
    line-height: 19px;
    color: var(--text-blue);
    margin-bottom: 21px;
  }
  .benefits li::before { content: "• "; color: var(--teal); }
  .contact-bar {
    position: absolute;
    left: 0; top: 1146px;
    width: 927px; height: 54px;
    background: var(--brand-blue);
    color: var(--white);
    font-family: "Montserrat", sans-serif;
    font-weight: 600;
    font-size: 20px;
    letter-spacing: 0.2em;
    display: flex;
    align-items: center;
    justify-content: center;
  }
</style>
</head>
<body>
<main class="flyer">
  <section class="hero">
    <svg width="927" height="830" viewBox="0 0 927 830" xmlns="http://www.w3.org/2000/svg">
      <defs>
        <linearGradient id="photoTone" x1="0" y1="0" x2="0" y2="1">
          <stop offset="0" stop-color="#d8dcdf"/>
          <stop offset="0.45" stop-color="#a9b1b8"/>
          <stop offset="1" stop-color="#8f9aa5"/>
        </linearGradient>
        <linearGradient id="blueWash" x1="0" y1="0" x2="0" y2="1">
          <stop offset="0" stop-color="#3b7fb6" stop-opacity="0"/>
          <stop offset="0.55" stop-color="#3b7fb6" stop-opacity="0.75"/>
          <stop offset="1" stop-color="#3577b0" stop-opacity="1"/>
        </linearGradient>
        <clipPath id="heroCurve">
          <path d="M0 0 H927 V700 C760 745 600 790 440 792 C280 794 120 770 0 742 Z"/>
        </clipPath>
      </defs>
      <path class="accent-curve" d="M0 742 C120 770 280 794 440 792 C600 790 760 745 927 700 V716 C760 762 600 808 440 808 C300 808 180 790 0 760 Z" fill="var(--teal)"/>
      <g clip-path="url(#heroCurve)">
        <rect role="img" aria-label="Photo of a technician in shoe covers steam-cleaning a grey carpet with an extraction wand" x="0" y="0" width="927" height="830" fill="url(#photoTone)"/>
        <rect x="0" y="380" width="927" height="450" fill="url(#blueWash)"/>
      </g>
    </svg>
    <div class="brand-panel">
      <div class="brand-mark" aria-hidden="true"></div>
      <div class="brand-name">
        <span class="brand-main">TIDEWELL</span>
        <span class="brand-sub">PROPERTY SERVICES</span>
      </div>
    </div>
    <div class="hero-copy">
      <h1 class="headline">Is your carpet in need<br>of a fresh start?</h1>
      <p class="subline">Whether you're a homeowner or a business owner, our<br>expert carpet cleaning services are here to<br>revitalize your space.</p>
    </div>
  </section>

  <section class="audiences">
    <div class="audience audience-residential">
      <h2 class="audience-title">For our<br>residential<br>customers</h2>
      <ul class="benefits">
        <li>Family and pets are messy - we understand! Let us restore the beauty of your home's carpets with our deep cleaning process.</li>
        <li>Our certified technicians use eco-friendly solutions that are safe for your loved ones and the environment.</li>
        <li>Enjoy a healthier living space with reduced allergens and odors.</li>
      </ul>
    </div>
    <div class="audience audience-commercial">
      <h2 class="audience-title">For our<br>commercial<br>customers</h2>
      <ul class="benefits">
        <li>First impressions matter! Elevate the appearance of your business with our professional carpet cleaning.</li>
        <li>We work around your schedule to minimize disruption to your daily operations.</li>
        <li>Impress your clients and create a comfortable workspace for your employees.</li>
      </ul>
    </div>
  </section>

  <footer class="contact-bar">CONTACT: 555-319-4826</footer>
</main>
</body>
</html>
```